Business Card Design - Will Pick Design in 24 Hours

I am looking for a simple, luxury, yet eye catching business card for my electronic business. The business is called Velmorix and I have attached the logo to this job.

The business card must have the following details:

1. Name
2. Email Address
3. Website
4. Position

```html
<!DOCTYPE html>
<html lang="en">
<head>
<meta charset="utf-8">
<title>Velmorix Business Card</title>
<link rel="stylesheet" href="https://fonts.googleapis.com/css2?family=Open+Sans:wght@400;600;700&display=swap">
<style>
  :root {
    --navy: #24344a;
    --white: #ffffff;
    --ink: #111111;
    --canvas: #e9ebee;
    --divider-glow: rgba(255, 255, 255, 0.35);
  }
  * { margin: 0; padding: 0; box-sizing: border-box; }
  html, body { width: 1200px; height: 900px; overflow: hidden; }
  body {
    background: var(--canvas);
    font-family: "Open Sans", sans-serif;
    display: flex;
    flex-direction: column;
    align-items: center;
    justify-content: center;
    gap: 40px;
  }
  .card {
    position: relative;
    width: 700px;
    height: 400px;
    border-radius: 14px;
    overflow: hidden;
    box-shadow: 0 8px 24px rgba(0,0,0,0.15);
  }
  .edge-band { position: absolute; top: 0; bottom: 0; width: 30px; }
  .edge-band.left { left: 0; }
  .edge-band.right { right: 0; }

  /* Front */
  .card-front { background: var(--white); }
  .card-front .edge-band { background: var(--navy); }
  .front-brand {
    position: absolute; inset: 0;
    display: flex; align-items: center; justify-content: center; gap: 18px;
  }
  .brand-mark { width: 34px; height: 34px; background: var(--ink); }
  .brand-name {
    font-weight: 600; font-size: 60px; letter-spacing: 4px;
    text-transform: uppercase; color: var(--ink);
  }

  /* Back */
  .card-back { background: var(--navy); color: var(--white); }
  .card-back .edge-band { background: var(--white); }
  .back-brand {
    position: absolute; left: 64px; top: 150px;
    display: flex; align-items: center; gap: 12px;
  }
  .back-brand .brand-mark { width: 20px; height: 20px; background: var(--white); }
  .back-brand .brand-name { font-size: 30px; letter-spacing: 2px; color: var(--white); }
  .divider-art {
    position: absolute; left: 308px; top: 40px;
    width: 8px; height: 320px;
    border-radius: 4px;
    background: linear-gradient(to bottom, transparent, var(--divider-glow) 50%, transparent);
  }
  .details { position: absolute; left: 360px; top: 70px; }
  .person-name { font-weight: 700; font-size: 27px; text-transform: uppercase; letter-spacing: 1px; }
  .person-role { font-size: 13px; text-transform: uppercase; letter-spacing: 1px; margin-top: 2px; }
  .contact-list { list-style: none; margin-top: 34px; }
  .contact-item {
    display: flex; align-items: flex-start; gap: 12px;
    font-size: 15px; line-height: 22px; margin-bottom: 12px;
  }
  .contact-icon { flex: none; margin-top: 4px; }
</style>
</head>
<body>
  <section class="card card-front">
    <div class="edge-band left"></div>
    <div class="edge-band right"></div>
    <div class="front-brand">
      <span class="brand-mark"></span>
      <span class="brand-name">Velmorix</span>
    </div>
  </section>

  <section class="card card-back">
    <div class="edge-band left"></div>
    <div class="edge-band right"></div>
    <div class="back-brand">
      <span class="brand-mark"></span>
      <span class="brand-name">Velmorix</span>
    </div>
    <div class="divider-art" role="img" aria-label="Decorative curved line divider"></div>
    <div class="details">
      <div class="person-name">Marcus Delvane</div>
      <div class="person-role">Executive Director</div>
      <ul class="contact-list">
        <li class="contact-item">
          <svg class="contact-icon" width="14" height="14" viewBox="0 0 14 14"><rect x="1" y="3" width="12" height="8" fill="none" stroke="#fff" stroke-width="1.3"/><path d="M1 3 L7 8 L13 3" fill="none" stroke="#fff" stroke-width="1.3"/></svg>
          <span>marcus@velmorixgroup.com</span>
        </li>
        <li class="contact-item">
          <svg class="contact-icon" width="14" height="14" viewBox="0 0 14 14"><circle cx="7" cy="7" r="5.5" fill="none" stroke="#fff" stroke-width="1.3"/><ellipse cx="7" cy="7" rx="2.3" ry="5.5" fill="none" stroke="#fff" stroke-width="1"/><line x1="1.5" y1="7" x2="12.5" y2="7" stroke="#fff" stroke-width="1"/></svg>
          <span>www.velmorixgroup.com</span>
        </li>
        <li class="contact-item">
          <svg class="contact-icon" width="14" height="14" viewBox="0 0 14 14"><path d="M1.5 7 L7 2 L12.5 7" fill="none" stroke="#fff" stroke-width="1.4"/><rect x="3.5" y="7" width="7" height="5.5" fill="#fff"/></svg>
          <span>2480 Harbor Crest Avenue,<br>4th Fl Lakeview, NY 10482</span>
        </li>
      </ul>
    </div>
  </section>
</body>
</html>
```